Business Card Design

Selling Televisions, Velmora, Kira, Dravelux, Ronavi
The latest models, sizes ranging from 22"- 75"
Surround Sounds, Sound Bars and Wall Mounts

Target Market(s)

Mainly males/boys/blokes etc

Industry/Entity Type

Business

Contact Information for Business Card

Glen Marsh
07841526094
glmarsh@quinvale-mail.com

Requirements
Must have
• simplistic design, probably just 2 of the images used

clarity essential
Nice to have
• Metallic if possible

```html
<!DOCTYPE html>
<html lang="en">
<head>
<meta charset="utf-8">
<title>Glen Marsh – Business Card</title>
<link rel="stylesheet" href="https://fonts.googleapis.com/css2?family=Cinzel:wght@400&family=Open+Sans:wght@400&display=swap">
<style>
  :root {
    --page-bg: #1b1b1c;
    --card-top: #3a3d40;
    --card-mid: #202325;
    --card-bottom: #121416;
    --band: #141618;
    --band-edge: #2c2f32;
    --accent-block: #0b0c0d;
    --teal: #3fc6cf;
    --text-light: #f2f4f5;
    --product-sky: #3b3f8a;
    --product-dusk: #b86e48;
    --product-city: #1c2350;
  }
  * { margin: 0; padding: 0; box-sizing: border-box; }
  html, body {
    width: 1200px; height: 944px; overflow: hidden;
    background: var(--page-bg);
  }
  .canvas {
    position: relative; width: 1200px; height: 944px;
    background: radial-gradient(ellipse at 50% 45%, #2a2a2b 0%, var(--page-bg) 70%);
  }
  .card {
    position: absolute; left: 150px; top: 215px;
    width: 900px; height: 514px; overflow: hidden;
    background: linear-gradient(160deg, var(--card-top) 0%, var(--card-mid) 45%, var(--card-bottom) 100%);
    box-shadow: 0 20px 50px rgba(0,0,0,0.6);
  }
  .card__accent-block {
    position: absolute; left: 600px; top: 118px; width: 300px; height: 110px;
    background: var(--accent-block);
  }
  .card__band {
    position: absolute; left: 0; top: 228px; width: 100%; height: 150px;
    background: linear-gradient(180deg, var(--band-edge) 0%, var(--band) 12%, var(--band) 88%, var(--band-edge) 100%);
  }
  .card__product {
    position: absolute; left: 460px; top: 60px; width: 390px; height: 290px;
    background: linear-gradient(180deg, var(--product-sky) 0%, var(--product-dusk) 40%, var(--product-city) 100%);
  }
  .card__details {
    position: absolute; left: 70px; top: 250px; width: 380px;
  }
  .card__name {
    font-family: "Cinzel", serif; font-weight: 400;
    font-size: 44px; letter-spacing: 2px; color: var(--teal);
    line-height: 1.1; white-space: nowrap;
  }
  .card__contact {
    list-style: none; margin-top: 10px; margin-left: 32px;
    font-family: "Open Sans", sans-serif; font-size: 20px;
    color: var(--text-light); line-height: 1.5; white-space: nowrap;
  }
  .card__contact-label { color: var(--teal); margin-right: 6px; }
</style>
</head>
<body>
<div class="canvas">
  <div class="card">
    <div class="card__accent-block"></div>
    <div class="card__band"></div>

    <div class="card__product" role="img" aria-label="Product photo: curved television on a stand showing a city at dusk"></div>

    <div class="card__details">
      <h1 class="card__name">Glen Marsh</h1>
      <ul class="card__contact">
        <li><span class="card__contact-label">P:</span>07841526094</li>
        <li><span class="card__contact-label">E:</span>glmarsh@quinvale-mail.com</li>
      </ul>
    </div>
  </div>
</div>
</body>
</html>
```